Singer/Song Writer on a Spirited Path needs Album Cover Design

I'm looking for a design for my Album titled: The Lantern Hour.
I would like to steer it away from the strictly "Christian" eschatology of "the Lantern Hour" and into the direction of these definitions of Rapture...
"intense bliss or beatitude"
"powerful emotion that lifts one out of oneself"
"a state or feeling of great happiness, pleasure, or love"

The 1st song on my album is named "Carry The Stone" And there's also a song titled "The Heron" to which the chorus is: "Consume me and free The Heron"
The album is compiled of songs about life's stuggles and triumphs/ pain and beauty/ ups and downs... with hopefully helpful words and sounds to ease our human condition.

I envision something like a Phoenix rising from the waters of life. But I don't want it to be too literally a Phoenix. I like The Heron as flames and not extremely birdlike. I like The Heron in file #1 the best... but like the half water, half phoenix in File 2.
The other 2 files are just to give some more ideas I've had that might be incorporated.
Thanks!

Reason: I needed a little more time, as I am sharing my project with my producer and my family... both of whom are out of the country. Thank you!

Other font styles liked:
• Depending on the design... I like 'Many Weatz' or 'Anaema' or 'Before the Rain' for the album title... "The Lantern Hour"

• My name: "Liesel"
• The album title: "The Lantern Hour"
• Not sure where this should appear:
• Produced/recorded at 'The Vault' in Montezuma, Costa Rica, with/by Ferrante

```html
<!DOCTYPE html>
<html lang="en">
<head>
<meta charset="utf-8">
<title>Liesel — The Lantern Hour</title>
<link href="https://fonts.googleapis.com/css2?family=Cinzel:wght@700&family=Great+Vibes&display=swap" rel="stylesheet">
<style>
  :root {
    --night: #000000;
    --deep-navy: #0a0b24;
    --indigo: #1a1440;
    --teal: #3fd3d0;
    --aqua: #7fe8e6;
    --ember: #ff8a1c;
    --flame: #ffc247;
    --ocean: #0c3f9a;
    --ocean-light: #2aa6c8;
    --gold-light: #fbe796;
    --gold: #dcae3e;
    --gold-dark: #a87318;
    --script-white: #ffffff;
  }
  html, body {
    margin: 0;
    padding: 0;
    width: 1200px;
    height: 1200px;
    overflow: hidden;
    background: var(--night);
  }
  .album-cover {
    position: relative;
    width: 1200px;
    height: 1200px;
    overflow: hidden;
    background: var(--night);
  }
  .cover-artwork {
    position: absolute;
    inset: 150px 0 0 0;
    background:
      radial-gradient(ellipse 22% 30% at 70% 30%, rgba(255,194,71,0.95), rgba(255,138,28,0.6) 45%, transparent 75%),
      radial-gradient(ellipse 22% 32% at 64% 68%, rgba(255,150,40,0.9), rgba(220,80,20,0.45) 50%, transparent 80%),
      radial-gradient(ellipse 10% 30% at 54% 58%, rgba(255,245,220,0.85), transparent 80%),
      radial-gradient(ellipse 26% 40% at 36% 48%, rgba(127,232,230,0.9), rgba(63,211,208,0.5) 45%, transparent 78%),
      radial-gradient(ellipse 25% 35% at 10% 45%, rgba(150,60,80,0.45), transparent 80%),
      linear-gradient(to bottom, transparent 0%, transparent 64%, rgba(42,166,200,0.75) 70%, var(--ocean) 82%, #0a2a6a 100%),
      linear-gradient(to bottom, var(--night) 0%, var(--deep-navy) 40%, var(--indigo) 70%);
  }
  .cover-title {
    position: absolute;
    top: 66px;
    left: 0;
    right: 0;
    display: flex;
    justify-content: center;
    align-items: baseline;
    gap: 36px;
    white-space: nowrap;
  }
  .artist-name {
    font-family: "Cinzel", serif;
    font-weight: 700;
    font-size: 66px;
    letter-spacing: 0.28em;
    margin-right: -0.28em;
    background: linear-gradient(to bottom, var(--gold-light) 0%, var(--gold) 55%, var(--gold-dark) 100%);
    -webkit-background-clip: text;
    background-clip: text;
    color: transparent;
  }
  .album-title {
    font-family: "Great Vibes", cursive;
    font-size: 90px;
    color: var(--script-white);
    line-height: 1;
  }
</style>
</head>
<body>
  <main class="album-cover">
    <div class="cover-artwork" role="img" aria-label="Cover artwork area in turquoise, amber and deep blue tones"></div>
    <header class="cover-title">
      <span class="artist-name">LIESEL</span>
      <span class="album-title">The Lantern Hour</span>
    </header>
  </main>
</body>
</html>
```